Pet label template for Corvantis mexican based company

Hello, Corvantis is a mexican based company dedicated to manufacture and sell its propietary brands for human health care. We are now introducing a new "Pet" category to our Brand. It´s name is Corvantis Pets (logo attached).
We are lookoig for the design template for our package labels that will most probably be in plastic bags like the example attaches (Kindle Paw of lakeshire). It is important to point out that the labels are going to be pasted on the bags and not directly printed on the bags itself like the examples attached.

I am attaching some examples but please feel free to innovate your own desing. I am also attaching the logo that must be in every label.

Target Market(s)

Pet owners basically dogs and cats.

Industry/Entity Type

Health Care

Font styles to use
Other font styles liked:
• something easy to read

Requirements
Must have
• We like both simple elegant designs and bright colorful ones son feel free to innovate.
Nice to have
• Illustration of both cat or dog for their product label.

```html
<!DOCTYPE html>
<html lang="en">
<head>
<meta charset="utf-8">
<title>Corvantis Pets – Immunity Label</title>
<link href="https://fonts.googleapis.com/css2?family=Fredoka:wght@600;700&family=Oswald:wght@500;600;700&display=swap" rel="stylesheet">
<style>
  :root {
    --backdrop: #e4e1de;
    --leaf-green: #56c62f;
    --leaf-green-light: #74d83e;
    --deep-green: #1f6b2c;
    --forest-text: #2f6e1a;
    --lime: #d8f23a;
    --ink: #1a1a1a;
    --white: #ffffff;
    --cat-grey: #7d7d80;
    --dog-brown: #7a4a26;
  }
  * { margin: 0; padding: 0; box-sizing: border-box; }
  html, body {
    width: 1200px; height: 1114px; overflow: hidden;
    background: var(--backdrop);
  }
  .label {
    position: absolute; left: 280px; top: 77px;
    width: 640px; height: 960px;
    background: var(--leaf-green);
    overflow: hidden;
    border-radius: 6px;
    box-shadow: 0 10px 30px rgba(0,0,0,0.12);
  }
  .label-curves { position: absolute; inset: 0; }
  .brand {
    position: absolute; top: 82px; left: 0; width: 100%;
    display: flex; justify-content: center; align-items: center; gap: 12px;
    font-family: "Oswald", sans-serif; font-weight: 600;
    font-size: 40px; letter-spacing: 2px; color: var(--white);
    text-transform: uppercase;
  }
  .brand-dot { width: 22px; height: 22px; border-radius: 50%; background: var(--white); }
  .product-name {
    position: absolute; top: 150px; left: 0; width: 100%;
    text-align: center;
    font-family: "Fredoka", sans-serif; font-weight: 700;
    font-size: 96px; line-height: 1; color: var(--white);
    letter-spacing: -1px;
    text-shadow: 0 0 0 var(--lime), 3px 3px 0 var(--lime);
  }
  .tagline-bar {
    position: absolute; top: 240px; left: 108px; width: 424px; height: 20px;
    background: var(--deep-green);
    color: var(--white);
    font-family: "Oswald", sans-serif; font-weight: 500;
    font-size: 12px; letter-spacing: 0.5px;
    display: flex; align-items: center; justify-content: center;
  }
  .key-ingredients {
    position: absolute; top: 280px; left: 0; width: 100%;
    text-align: center;
    font-family: "Oswald", sans-serif; font-weight: 600;
    font-size: 23px; letter-spacing: 0.5px; color: var(--ink);
  }
  .benefits { position: absolute; top: 326px; left: 168px; list-style: none; }
  .benefit {
    display: flex; align-items: center; gap: 10px;
    height: 36px; margin-bottom: 0;
  }
  .benefit-icon { width: 30px; height: 30px; flex: none; }
  .benefit-text {
    font-family: "Oswald", sans-serif; font-weight: 500;
    font-size: 18px; color: var(--white);
    padding: 2px 4px 3px 0; min-width: 220px;
    border-bottom: 2px dotted rgba(255,255,255,0.7);
  }
  .benefit-text::before { content: "✓ "; font-size: 14px; }
  .pets-illustration {
    position: absolute; left: 218px; top: 478px; width: 310px; height: 262px;
    border-radius: 40px 60px 10px 10px;
    background: linear-gradient(90deg, var(--cat-grey) 0%, var(--cat-grey) 30%, var(--dog-brown) 55%, var(--dog-brown) 100%);
    opacity: 0.9;
  }
  .grain-free {
    position: absolute; top: 748px; left: 196px;
    font-family: "Oswald", sans-serif; font-weight: 700;
    font-size: 25px; color: var(--forest-text); line-height: 1;
  }
  .net-weight {
    position: absolute; top: 778px; left: 196px;
    font-family: "Oswald", sans-serif; font-weight: 600;
    font-size: 13px; color: var(--forest-text);
  }
</style>
</head>
<body>
  <main class="label">
    <svg class="label-curves" width="640" height="960" viewBox="0 0 640 960" aria-hidden="true">
      <defs>
        <linearGradient id="lime-sweep" x1="0" y1="1" x2="1" y2="0">
          <stop offset="0" stop-color="#6fd23a"/>
          <stop offset="0.6" stop-color="#e3f53a"/>
          <stop offset="1" stop-color="#b6e93a"/>
        </linearGradient>
      </defs>
      <path d="M0 770 C 110 560 360 400 640 388 L640 960 L0 960 Z" fill="#8fdc52"/>
      <path d="M0 800 C 120 585 370 425 640 414 L640 960 L0 960 Z" fill="url(#lime-sweep)"/>
      <path d="M20 830 C 140 615 380 448 640 432 L640 960 L20 960 Z" fill="var(--white)"/>
      <path d="M0 960 L0 800 C 8 790 14 810 20 830 L20 960 Z" fill="var(--leaf-green)"/>
    </svg>

    <div class="brand"><span class="brand-dot"></span>Corvantis Pets</div>
    <h1 class="product-name">Immunity</h1>
    <div class="tagline-bar">IMMUNE SUPPORT FOR PETS</div>
    <p class="key-ingredients">PROBIOTICS • VITAMINS • ANTIOXIDANTS</p>

    <ul class="benefits">
      <li class="benefit">
        <svg class="benefit-icon" viewBox="0 0 30 30" aria-hidden="true">
          <path d="M15 2 L26 6 V14 C26 21 21 26 15 28 C9 26 4 21 4 14 V6 Z" fill="none" stroke="#fff" stroke-width="2.4"/>
          <path d="M10 15 L14 19 L21 11" fill="none" stroke="#fff" stroke-width="2.6" stroke-linecap="round"/>
        </svg>
        <span class="benefit-text">SUPPORT IMMUNE SYSTEM</span>
      </li>
      <li class="benefit">
        <svg class="benefit-icon" viewBox="0 0 30 30" aria-hidden="true">
          <path d="M15 26 C6 19 2 15 2 10 C2 6 5 3 9 3 C12 3 14 5 15 7 C16 5 18 3 21 3 C25 3 28 6 28 10 C28 15 24 19 15 26 Z" fill="none" stroke="#fff" stroke-width="2.2"/>
          <path d="M4 14 H10 L12 10 L15 18 L17 13 H26" fill="none" stroke="#fff" stroke-width="2"/>
        </svg>
        <span class="benefit-text">CARDIOVASCULAR SYSTEM</span>
      </li>
      <li class="benefit">
        <svg class="benefit-icon" viewBox="0 0 30 30" aria-hidden="true">
          <path d="M3 10 C3 5 10 4 17 5 C24 6 28 8 27 12 C26 16 20 17 16 20 C12 23 9 26 7 24 C4 21 3 15 3 10 Z" fill="#fff"/>
        </svg>
        <span class="benefit-text">LIVER FUNCTION</span>
      </li>
    </ul>

    <div class="pets-illustration" role="img" aria-label="Illustration of a grey cat sitting beside a brown dog"></div>

    <p class="grain-free">GRAIN FREE</p>
    <p class="net-weight">NET WT 2.12 OZ. (90G)</p>
  </main>
</body>
</html>
```